Velmar Intergrated Marketing Stationary Design Contest

We require a very professional looking stationary set to include: letterhead, compliments slip and business cards (double sided bus cards).

Files should be supplied on either Illustrator or InDesign.

We are interested in perhaps encorporating a faint watermark with the letter q or the logo, but it isnt a pre-requisite

Target Market(s)

Business owners seeking professional marketing services

Industry/Entity Type

Marketing

Requirements
Must have
• Concurrent theme wiht business cards, letterhead and comp slip. Must be an editable document for future ammendment
Should not have
• No use of times new roman or similar fonts

```html
<!DOCTYPE html>
<html lang="en">
<head>
<meta charset="utf-8">
<title>Velmar Intergrated Marketing – Stationery Set</title>
<link rel="stylesheet" href="https://fonts.googleapis.com/css2?family=Open+Sans:ital,wght@0,400;0,600;0,700;1,600&display=swap">
<style>
  :root {
    --brand-orange: #f05a28;
    --ink: #1a1a1a;
    --mark-grey: #3b3b3b;
    --paper: #ffffff;
    --edge: #333333;
  }
  * { margin: 0; padding: 0; box-sizing: border-box; }
  html, body { width: 1200px; height: 1200px; overflow: hidden; background: var(--paper); }
  body { position: relative; font-family: "Open Sans", Arial, sans-serif; color: var(--ink); }

  .sheet { position: absolute; background: var(--paper); border: 1.2px solid var(--edge); }
  .letterhead { left: 181px; top: 32px; width: 651px; height: 920px; }
  .comp-slip { left: 347px; top: 240px; width: 650px; height: 307px; }
  .card-front { left: 292px; top: 979px; width: 279px; height: 171px; border-width: 1px; }
  .card-back { left: 616px; top: 979px; width: 278px; height: 171px; background: var(--brand-orange); border: none; }

  .brand-mark { position: absolute; display: flex; align-items: center; gap: 8px; }
  .brand-mark .dot { width: 30px; height: 30px; border-radius: 50%; background: var(--brand-orange); }
  .brand-mark .name { font-size: 27px; font-weight: 400; color: var(--mark-grey); letter-spacing: 3px; line-height: 1; }
  .letterhead .brand-mark { left: 35px; top: 42px; }
  .comp-slip .brand-mark { left: 35px; top: 38px; }
  .card-front .brand-mark { left: 14px; top: 78px; gap: 5px; }
  .card-front .brand-mark .dot { width: 18px; height: 18px; }
  .card-front .brand-mark .name { font-size: 15px; letter-spacing: 1.5px; }

  .slip-title { position: absolute; left: 70px; top: 80px; font-size: 15px; font-weight: 600; font-style: italic; color: var(--brand-orange); }

  .contact { position: absolute; text-align: right; font-size: 8.2px; line-height: 11px; }
  .letterhead .contact { right: 28px; top: 35px; }
  .comp-slip .contact { right: 29px; top: 28px; }
  .contact .company { color: var(--brand-orange); font-weight: 700; }
  .contact .gap { margin-top: 7px; }
  .label { color: var(--brand-orange); }
  .sep { display: inline-block; width: 8px; }

  .card-details { position: absolute; left: 132px; top: 45px; font-size: 6.4px; line-height: 8.6px; }
  .card-details .person { font-size: 11px; font-weight: 700; color: var(--brand-orange); line-height: 12px; }
  .card-details .role { font-size: 7.5px; line-height: 9px; }
  .card-details .company { color: var(--brand-orange); font-weight: 700; margin-top: 13px; }
  .card-details .gap { margin-top: 7px; }

  .card-back .back-name { position: absolute; right: 18px; bottom: 18px; font-size: 26px; font-weight: 400; color: var(--paper); letter-spacing: 2px; }
</style>
</head>
<body>

<section class="sheet letterhead" aria-label="Letterhead">
  <div class="brand-mark"><span class="dot"></span><span class="name">Velmar</span></div>
  <div class="contact">
    <div class="company">Velmar Intergrated Marketing</div>
    <div>Central Offices</div>
    <div>Harlow Street, Brackenford, West Riding, BR4 7QN</div>
    <div class="gap"><span class="label">W:</span> www.velmarim.co.uk <span class="sep"></span><span class="label">E:</span> enquiries@velmarim.co.uk</div>
    <div><span class="label">T:</span> 01632 960614 <span class="sep"></span><span class="label">F:</span> 01632 960611</div>
    <div class="gap">Company registration: 4815162 <span class="sep"></span>Vat No: 771 2048 55</div>
    <div>Trading as a division of Brindle Ltd</div>
  </div>
</section>

<section class="sheet comp-slip" aria-label="Compliments slip">
  <div class="brand-mark"><span class="dot"></span><span class="name">Velmar</span></div>
  <div class="slip-title">WITH COMPLEMENTS</div>
  <div class="contact">
    <div class="company">Velmar Intergrated Marketing</div>
    <div>Central Offices</div>
    <div>Harlow Street, Brackenford, West Riding, BR4 7QN</div>
    <div class="gap"><span class="label">W:</span> www.velmarim.co.uk <span class="sep"></span><span class="label">E:</span> enquiries@velmarim.co.uk</div>
    <div><span class="label">T:</span> 01632 960614 <span class="sep"></span><span class="label">F:</span> 01632 960611</div>
    <div class="gap">Company registration: 4815162 <span class="sep"></span>Vat No: 771 2048 55</div>
    <div>Trading as a division of Brindle Ltd</div>
  </div>
</section>

<section class="sheet card-front" aria-label="Business card front">
  <div class="brand-mark"><span class="dot"></span><span class="name">Velmar</span></div>
  <div class="card-details">
    <div class="person">Tom Hadley</div>
    <div class="role">General Manager</div>
    <div class="company">Velmar Intergrated Marketing</div>
    <div>Central Offices</div>
    <div>Harlow Street, Brackenford, West Riding</div>
    <div>BR4 7QN</div>
    <div class="gap"><span class="label">W:</span> www.velmarim.co.uk</div>
    <div><span class="label">E:</span> tom@velmarim.co.uk</div>
    <div><span class="label">T:</span> 01632 960614</div>
    <div><span class="label">F:</span> 01632 960611</div>
  </div>
</section>

<section class="sheet card-back" aria-label="Business card back">
  <span class="back-name">Velmar</span>
</section>

</body>
</html>
```